You are cordially invited to attend a delicious Afternoon Tea at The Harcourt.

Enjoy a glass of sparkling wine whilst afternoon delicacies and a menu of fine teas is presented for you to enjoy throughout the afternoon.

This is an opportunity to get together with a table of like minded ladies just for fun and to share some stories and meet some new friends.

Date: 8 August 2014
Time: 12pm - 2pm
Venue: 48 Larkmoor Lane, Melbourne VIC 3000

(hello please see above text we require - we would like to invite our clients to an afternoon tea, an invitation (hard copy) to be of elegant taste, nice lettering, pic added to the invite).

```html
<!DOCTYPE html>
<html lang="en">
<head>
<meta charset="utf-8">
<title>Afternoon Tea at The Harcourt</title>
<link rel="stylesheet" href="https://fonts.googleapis.com/css2?family=Raleway:wght@400;500&display=swap">
<style>
  :root {
    --photo-light: #efe6da;
    --photo-warm: #d9c7ae;
    --photo-shade: #8f8a82;
    --band-dark: rgba(72, 70, 68, 0.62);
    --band-soft: rgba(214, 209, 203, 0.82);
    --footer-bg: #d8d5d2;
    --ink-light: #f4f1ec;
    --ink-dark: #3b3632;
    --ink-mid: #5b5550;
    --ink-pale: #a19d99;
  }
  * { margin: 0; padding: 0; box-sizing: border-box; }
  html, body { width: 1200px; height: 780px; overflow: hidden; background: #ffffff; }
  body { font-family: "Raleway", sans-serif; }
  .invitation { position: relative; width: 1200px; height: 780px; background: var(--footer-bg); }
  .hero-photo {
    position: absolute; left: 0; top: 0; width: 1200px; height: 615px;
    background:
      radial-gradient(ellipse 260px 300px at 560px 180px, #fff8ec 0%, rgba(255,248,236,0) 70%),
      radial-gradient(ellipse 200px 260px at 400px 160px, rgba(200,70,70,0.35) 0%, rgba(200,70,70,0) 70%),
      linear-gradient(90deg, var(--photo-shade) 0%, var(--photo-warm) 30%, var(--photo-light) 50%, var(--photo-warm) 75%, var(--photo-shade) 100%);
  }
  .details-band {
    position: absolute; left: 0; top: 354px; width: 1200px; height: 111px;
    background: var(--band-dark);
    padding: 10px 0 0 4px;
    color: var(--ink-light); font-size: 17px; line-height: 22px;
  }
  .welcome-band {
    position: absolute; left: 0; top: 465px; width: 1200px; height: 150px;
    background: var(--band-soft);
    text-align: center;
  }
  .welcome-band .headline { margin-top: 14px; font-size: 22px; font-weight: 500; color: var(--ink-dark); }
  .welcome-band .offer { margin-top: 26px; font-size: 19px; line-height: 24px; color: var(--ink-mid); }
  .closing-band {
    position: absolute; left: 0; top: 615px; width: 1200px; height: 165px;
    text-align: center; padding-top: 24px;
    font-size: 19px; line-height: 25px; color: var(--ink-pale);
  }
</style>
</head>
<body>
<main class="invitation">
  <div class="hero-photo" role="img" aria-label="Photograph of an afternoon tea table with a tiered cake stand, teacups and glasses in a softly lit room"></div>
  <section class="details-band">
    <p>Date: 8 August 2014</p>
    <p>Time: 12pm - 2pm</p>
    <p>Venue: 48 Larkmoor Lane, Melbourne VIC 3000</p>
  </section>
  <section class="welcome-band">
    <h1 class="headline">You are cordially invited to attend a delicious Afternoon Tea at The Harcourt</h1>
    <p class="offer">Enjoy a glass of sparkling wine whilst afternoon delicacies and a menu of fine teas<br>is presented for you<br>to enjoy throughout the afternoon</p>
  </section>
  <section class="closing-band">
    <p>This is an opportunity<br>to get together with a table of like minded ladies just for fun and to share some stories<br>and meet some new friends</p>
  </section>
</main>
</body>
</html>
```